Web Design Brochure

We want a brochure, that we can email and also be sent to our printers. I've attached our logo and content for the brochure. Our websites are www.velmaro.co.uk and www.velmaro-franchise.co.uk
We would want the source files as part of the deal.
Updates

We only need a nice simple design. Just one brochure not an email aswell. We can email the brochure. We have a number of designers in house who are tied up on a big project. They tell me they could put something together in an hour or so. So £30 we feel is ample for a quick and simple project.

Target Market(s)

businesses

Industry/Entity Type

Advertising

```html
<!DOCTYPE html>
<html lang="en">
<head>
<meta charset="utf-8">
<title>Websites – Pricing Brochure</title>
<link href="https://fonts.googleapis.com/css2?family=Josefin+Sans:wght@300&family=Questrial&display=swap" rel="stylesheet">
<style>
  :root {
    --teal: #4e8b8f;
    --page: #f5fafb;
    --edge: #d3e8ef;
    --ink: #2b2b2b;
    --white: #ffffff;
  }
  * { margin: 0; padding: 0; box-sizing: border-box; }
  html, body { width: 900px; height: 1200px; overflow: hidden; }
  body {
    background: var(--page);
    font-family: "Questrial", "Century Gothic", sans-serif;
    color: var(--ink);
    position: relative;
  }
  .edge { position: absolute; top: 0; bottom: 0; width: 12px; background: var(--edge); }
  .edge--left { left: 0; }
  .edge--right { right: 0; }

  .masthead {
    position: absolute;
    right: 6px;
    top: -6px;
    font-family: "Josefin Sans", "Century Gothic", sans-serif;
    font-weight: 300;
    font-size: 176px;
    line-height: 1;
    letter-spacing: -4px;
    color: var(--teal);
  }

  .band {
    position: absolute;
    left: 12px;
    right: 0;
    height: 32px;
    background: var(--teal);
    color: var(--white);
    font-size: 25px;
    line-height: 32px;
    padding-left: 28px;
    white-space: nowrap;
  }
  .band--half { top: 144px; }
  .band--brochure { top: 262px; }
  .band--shop { top: 608px; }
  .band--bespoke { top: 1045px; padding-left: 22px; }

  .copy {
    position: absolute;
    left: 41px;
    width: 790px;
    font-size: 14.5px;
    line-height: 20px;
  }
  .copy--half { top: 201px; }
  .list { list-style: none; }
  .list li::before { content: "• "; }
  .list--pages { top: 311px; line-height: 20px; }
  .copy--brochure { top: 426px; width: 800px; }
  .subhead {
    position: absolute;
    left: 41px;
    top: 505px;
    font-size: 21px;
    line-height: 26px;
  }
  .copy--extras { top: 543px; width: 760px; }
  .copy--shop { top: 666px; width: 800px; }
  .list--features { top: 718px; line-height: 17.6px; }
  .copy--products { top: 890px; width: 810px; }
  .pull-quote {
    position: absolute;
    left: 41px;
    top: 966px;
    width: 800px;
    font-size: 18.5px;
    line-height: 23px;
  }
  .copy--bespoke { top: 1099px; left: 34px; }
</style>
</head>
<body>
  <div class="edge edge--left"></div>
  <div class="edge edge--right"></div>

  <h1 class="masthead">WEBSITES</h1>

  <h2 class="band band--half">1/2 page website £200 or £20pm</h2>
  <p class="copy copy--half">Brilliant for creating simple professional business website to personal interest and hobby web pages or<br>even selling a property</p>

  <h2 class="band band--brochure">4/5 page brochure style website £500 or £35pm</h2>
  <ul class="copy list list--pages">
    <li>Home Page</li>
    <li>Products page</li>
    <li>Services page</li>
    <li>About us page</li>
    <li>Contact us page</li>
  </ul>
  <p class="copy copy--brochure">‘Brochure Style’ refers to a basic HTML website or basic website design. A simple website will provide your client with an online web presence. Brochure style website design can be tailored to your clients exact requirement and provide their business with an entry level website platform to showcase their products or services online. You can be as innovative and creative as you desire with this basic website</p>

  <h3 class="subhead">Additional Functionality £100 or £10pm</h3>
  <p class="copy copy--extras">Additional functionality such as basic forums and blogs are available at £100 or £10 per month. Any advanced functionality would fall into our bespoke packages.</p>

  <h2 class="band band--shop">Ecommerce Website £1000</h2>
  <p class="copy copy--shop">Our scalable custom built online store ecommerce solutions can incorporate the following features based on customer's requirements:</p>
  <ul class="copy list list--features">
    <li>Allows your customer to browse a limitless number of online products and product categories.</li>
    <li>Customers can add/remove and modify products to their online shopping cart.</li>
    <li>Intuitive checkout system minimizes online shopping cart abandonment.</li>
    <li>Automatically generates and emails a Tax Invoice to your customer.</li>
    <li>SSL 128bit encryption for secure online transactions.</li>
    <li>Complete online inventory management along with ecommerce.</li>
    <li>Online order management systems.</li>
    <li>Third party payment gateway integration with the ecommerce system.</li>
    <li>Search Engine friendly catalogues and content management systems</li>
  </ul>
  <p class="copy copy--products">Display featured products with an image, price, strap-line and short description. Choose which products you would like displayed and how they should be arranged. Whatever you call it; shopping online, e-Commerce, web purchasing... buying products, services and electronic downloads via a website is a growing business.</p>
  <p class="pull-quote">The only definite thing that will happen to online purchases is that they will continue to grow over the coming years</p>

  <h2 class="band band--bespoke">Bespoke website £negotiable prices start from £1000</h2>
  <p class="copy copy--bespoke">Bespoke websites cover a whole spectrum of different styles of including Social networking site, forums, blog.</p>
</body>
</html>
```